Skincare company needing leaflet/flyer for selling products

Hi guys. I am needing a leaflet/flyer design for my new skincare business - Tovani skincare. Our products are all made in Australia from natural ingredients. The leaflet should specify that all products have - organic ingredients, cruelty free, no nasty chemicals or ingredients and a made in Australia logo.
The pictures I have supplied, if they can be made more professional looking for the design without any background that would be great. It should look like other competitors and very appealing. The leaflet can be double sided so it looks more easy to read
The information is provided as follows:
Product, skin types the product is for, ml capacity of bottle, key ingredients and price.
Contact is a whatsapp number and website will be up later so if a leaflet can be made with and without the website.
This leaflet/flyer can be easy to read, not hard on the eyes and easy to understand. Focus on blue shades and other calm colours to make it easy on the eyes and attractive to see. Thank you guys for helping
Getting professional product photos done that can be updated on the leaflet/flyers once received. More submissions are welcomed
People wanting good quality skincare that does not contain harmful chemicals and is organic

```html
<!DOCTYPE html>
<html lang="en">
<head>
<meta charset="utf-8">
<title>Tovani Skincare – Product Leaflet</title>
<link rel="stylesheet" href="https://fonts.googleapis.com/css2?family=Lora:ital,wght@0,400;0,600;1,600;1,700&display=swap">
<style>
  :root {
    --navy: #1b2136;
    --ink: #2a2e3a;
    --grey-light: #e4e4e6;
    --grey-mid: #b9b9bd;
    --grey-dark: #8d8d93;
    --paper: #ffffff;
    --backdrop: #f1f1f2;
  }
  * { margin: 0; padding: 0; box-sizing: border-box; }
  html, body { width: 1200px; height: 2280px; overflow: hidden; }
  body {
    background: var(--backdrop);
    position: relative;
    font-family: "Lora", Georgia, serif;
    color: var(--ink);
  }
  .page {
    position: absolute;
    left: 232px;
    width: 735px;
    height: 1043px;
    background: var(--paper);
    overflow: hidden;
  }
  .page--front { top: 79px; }
  .page--back { top: 1162px; }

  /* Front */
  .brand-square {
    position: absolute; left: 259px; top: 34px;
    width: 217px; height: 215px;
    background: var(--navy);
  }
  .brand-name {
    position: absolute; left: 0; width: 100%; text-align: center;
    color: var(--navy); font-weight: 400; text-transform: uppercase;
  }
  .brand-name--main { top: 275px; font-size: 86px; letter-spacing: 16px; padding-left: 16px; }
  .brand-name--sub { top: 392px; font-size: 34px; letter-spacing: 11px; padding-left: 11px; }

  .promise {
    position: absolute; top: 556px; width: 150px; margin-left: -75px;
    text-align: center;
  }
  .promise__icon {
    width: 110px; height: 110px; margin: 0 auto;
    border-radius: 50%;
    border: 2px solid var(--navy);
    display: flex; align-items: center; justify-content: center;
  }
  .promise__icon span {
    width: 84px; height: 84px; border-radius: 50%;
    background: var(--grey-light);
  }
  .promise__label {
    margin-top: 12px; font-size: 14px; line-height: 18px;
    color: var(--ink); text-transform: uppercase;
  }
  .front-scenery { position: absolute; left: 0; top: 752px; }
  .front-contact {
    position: absolute; top: 898px; color: var(--paper);
    font-size: 17px; text-align: center;
  }
  .front-contact svg { display: block; margin: 0 auto 14px; }

  /* Back */
  .product { position: absolute; width: 330px; }
  .product__title {
    height: 28px; background: var(--navy); color: var(--paper);
    font-style: italic; font-weight: 700; font-size: 21px; line-height: 28px;
    padding-left: 41px; border-radius: 0 14px 14px 0;
    margin-bottom: 8px;
  }
  .product--right .product__title { padding-left: 18px; }
  .product__body { padding-left: 41px; font-size: 10px; line-height: 12px; }
  .product--right .product__body { padding-left: 18px; }
  .product__meta { margin-bottom: 12px; }
  .product__key {
    font-style: italic; font-weight: 600; font-size: 11.5px; margin-bottom: 10px;
  }
  .ingredient__name { font-weight: 600; text-transform: uppercase; font-size: 9.5px; }
  .ingredient__name::before {
    content: ""; display: inline-block; width: 5px; height: 5px;
    background: var(--ink); margin-right: 4px; vertical-align: 1px;
  }
  .ingredient__text { padding-left: 20px; margin-bottom: 1px; max-width: 310px; }

  .back-scenery { position: absolute; left: 0; top: 0; }
  .contact-block {
    position: absolute; left: 526px; top: 879px; color: var(--paper); font-size: 12px;
  }
  .contact-block h3 { font-size: 15px; font-weight: 600; margin-bottom: 14px; }
  .contact-block p { margin-bottom: 14px; }
  .contact-block li { list-style: none; line-height: 15px; display: flex; align-items: center; gap: 6px; }
</style>
</head>
<body>

<section class="page page--front">
  <div class="brand-square"></div>
  <div class="brand-name brand-name--main">Tovani</div>
  <div class="brand-name brand-name--sub">Skincare</div>

  <div class="promise" style="left:205px">
    <div class="promise__icon" role="img" aria-label="Icon: seedling with heart leaves"><span></span></div>
    <p class="promise__label">% 100<br>Organic</p>
  </div>
  <div class="promise" style="left:367px">
    <div class="promise__icon" role="img" aria-label="Icon: three leaves"><span></span></div>
    <p class="promise__label">Cruelty<br>Free</p>
  </div>
  <div class="promise" style="left:532px">
    <div class="promise__icon" role="img" aria-label="Icon: laboratory flask"><span></span></div>
    <p class="promise__label">Chemicals<br>Free</p>
  </div>

  <svg class="front-scenery" width="735" height="291" viewBox="0 0 735 291" role="img" aria-label="Soft grey brushstroke mountain landscape">
    <defs>
      <linearGradient id="hills" x1="0" y1="0" x2="1" y2="1">
        <stop offset="0" stop-color="#a9a9ae"/>
        <stop offset="1" stop-color="#cfcfd3"/>
      </linearGradient>
    </defs>
    <path d="M0 60 C120 40 300 80 420 50 C470 20 520 0 560 10 C620 30 680 70 735 90 L735 291 L0 291 Z" fill="url(#hills)"/>
  </svg>

  <div class="front-contact" style="left:90px; width:150px">
    <svg width="30" height="30" viewBox="0 0 24 24" fill="none" stroke="#fff" stroke-width="1.6" aria-hidden="true">
      <path d="M5 3h4l2 5-2.5 1.5a11 11 0 0 0 6 6L16 13l5 2v4a2 2 0 0 1-2 2A17 17 0 0 1 3 5a2 2 0 0 1 2-2z"/>
    </svg>
    0400 318 752
  </div>
  <div class="front-contact" style="left:400px; width:230px">
    <svg width="30" height="30" viewBox="0 0 24 24" fill="none" stroke="#fff" stroke-width="1.4" aria-hidden="true">
      <circle cx="12" cy="12" r="10"/><ellipse cx="12" cy="12" rx="4.5" ry="10"/><path d="M2 12h20M4 7h16M4 17h16"/>
    </svg>
    www.tovaniskincare.com
  </div>
</section>

<section class="page page--back">
  <svg class="back-scenery" width="735" height="1043" viewBox="0 0 735 1043" role="img" aria-label="Grey brushstroke mountain peak">
    <defs>
      <linearGradient id="peak" x1="0" y1="1" x2="1" y2="0">
        <stop offset="0" stop-color="#76767d"/>
        <stop offset="1" stop-color="#a4a4aa"/>
      </linearGradient>
    </defs>
    <path d="M432 1043 L452 990 L488 940 L500 880 L540 840 L600 800 L660 768 L700 790 L735 820 L735 1043 Z" fill="url(#peak)"/>
  </svg>

  <article class="product" style="left:0; top:46px">
    <h2 class="product__title">Hydrating Moisturiser</h2>
    <div class="product__body">
      <p class="product__meta">60ml<br>$18<br>Normal/Dry/Mature Skin Types</p>
      <p class="product__key">Key Ingredients</p>
      <p class="ingredient__name">Rosehip Oil</p>
      <p class="ingredient__text">Rich in essential fatty acids which are integral for skin regeneration and boosting collagen formation.</p>
      <p class="ingredient__name">Green Tea Leaf Extract</p>
      <p class="ingredient__text">Anti-inflammatory benefits which reduce redness and soothes skin irritation.</p>
      <p class="ingredient__name">Davidson Plum Extract</p>
      <p class="ingredient__text">Improves the appearance of fine lines and wrinkles and rich in antioxidants.</p>
    </div>
  </article>

  <article class="product product--right" style="left:371px; top:46px">
    <h2 class="product__title">Balancing Moisturiser</h2>
    <div class="product__body">
      <p class="product__meta">60ml<br>$18<br>Oily | Combination | Problematic Skin Types</p>
      <p class="product__key">Key Ingredients</p>
      <p class="ingredient__name">Grape Seed Oil</p>
      <p class="ingredient__text">Acts as an anti-inflammatory and effective in combating acne.</p>
      <p class="ingredient__name">Licorice Root Extract</p>
      <p class="ingredient__text">Provides skin brightening effects and soothes itchy and irritated skin.</p>
      <p class="ingredient__name">Quandong (Sandalwood) Extract</p>
      <p class="ingredient__text">High in vitamin C, reduces the appearance of ageing such as dark circles and pigmentation.</p>
    </div>
  </article>

  <article class="product" style="left:0; top:277px">
    <h2 class="product__title">Eye Cream</h2>
    <div class="product__body">
      <p class="product__meta">15 ML<br>$19<br>All Skin Types</p>
      <p class="product__key">Key Ingredients</p>
      <p class="ingredient__name">Cucumis Sativus (Cucumber) Seed Oil</p>
      <p class="ingredient__text">Highly moisturising with Vitamin E, it balances the skin &amp; encourages healthy skin regeneration.</p>
      <p class="ingredient__name">Kakadu Plum Extract</p>
      <p class="ingredient__text">Rich in Vitamin C &amp; Gallic acid which has anti-inflammatory properties, can help reduce pigmentation and dark spots.</p>
      <p class="ingredient__name">Quandong Extract</p>
      <p class="ingredient__text">High in Rutin, an antioxidant that soothes skin and calms redness, it also reduces the signs of ageing.</p>
    </div>
  </article>

  <article class="product product--right" style="left:371px; top:277px">
    <h2 class="product__title">Facial Cleansing Gel</h2>
    <div class="product__body">
      <p class="product__meta">125ML<br>$20<br>Oily | Combination | Problematic Skin Types</p>
      <p class="product__key">Key Ingredients</p>
      <p class="ingredient__name">Vitamin E</p>
      <p class="ingredient__text">A natural antioxidant that helps to protect the face from exposure to the sun and increases skin elasticity. It also reduces acne, blemishes and soothes the skin.</p>
      <p class="ingredient__name">Aloe Vera Juice</p>
      <p class="ingredient__text">Hydrates &amp; exfoliates the face, reducing inflammation, acne and dry skin.</p>
      <p class="ingredient__name">Kakadu Plum Extract</p>
      <p class="ingredient__text">Rich in Vitamin C &amp; Gallic acid which has anti-inflammatory properties, can help reduce pigmentation and dark spots. Also stimulates growth of collagen.</p>
    </div>
  </article>

  <article class="product" style="left:0; top:535px">
    <h2 class="product__title">Vitamin C Serum</h2>
    <div class="product__body">
      <p class="product__meta">30ML<br>$15<br>All Skin types</p>
      <p class="product__key">Key Ingredients</p>
      <p class="ingredient__name">Sodium Phytate</p>
      <p class="ingredient__text">Contains stabilising properties that moisturises the skin, helps reduce pore size and improve the appearance of cellulite.</p>
      <p class="ingredient__name">Davidson Plum Extract</p>
      <p class="ingredient__text">Improves the appearance of fine lines and wrinkles and rich in antioxidants.</p>
      <p class="ingredient__name">Vitamin C (Sodium Ascorbyl Phosphate)</p>
      <p class="ingredient__text">Contains anti-inflammatory and anti-ageing properties and helps fight acne and blemishes.</p>
    </div>
  </article>

  <article class="product product--right" style="left:371px; top:535px">
    <h2 class="product__title">Perfecting Toning Mist</h2>
    <div class="product__body">
      <p class="product__meta">125ML<br>$17.50<br>All Skin Types</p>
      <p class="product__key">Key Ingredients</p>
      <p class="ingredient__name">Rose Flower Water</p>
      <p class="ingredient__text">Contains anti-ageing properties, hydrates the skin and soothes skin irritation.</p>
      <p class="ingredient__name">Green Tea Leaf Extract</p>
      <p class="ingredient__text">Anti-inflammatory benefits which reduce redness and soothes skin irritation.</p>
      <p class="ingredient__name">Kakadu Plum</p>
      <p class="ingredient__text">Rich in Vitamin C &amp; Gallic acid which has anti-inflammatory properties, can reduce pigmentation and dark spots. It also stimulates growth of collagen and reduces wrinkles.</p>
    </div>
  </article>

  <article class="product" style="left:0; top:774px; width:400px">
    <h2 class="product__title" style="width:186px">Body Balm</h2>
    <div class="product__body">
      <p class="product__meta">$18<br>250ML<br>All skin types</p>
      <p class="product__key">Key Ingredients</p>
      <p class="ingredient__name">Kakadu Plum Extract</p>
      <p class="ingredient__text" style="max-width:360px">Rich in Vitamin C &amp; Gallic acid which has anti-inflammatory properties, can help reduce pigmentation and dark spots. Also stimulates growth of collagen.</p>
      <p class="ingredient__name">Panthenol (Vitamin B5)</p>
      <p class="ingredient__text" style="max-width:360px">An anti-inflammatory skin barrier repairer that improves the appearance of skin, preventing dryness and keeping the skin balanced.</p>
      <p class="ingredient__name">Desert Lime Extract</p>
      <p class="ingredient__text" style="max-width:360px">High in Vitamin C &amp; antioxidants, it vitalises the skin, keeping it nourished and rejuvenated.</p>
    </div>
  </article>

  <div class="contact-block">
    <h3>Contact Us</h3>
    <p>Tovani Skincare</p>
    <ul>
      <li><svg width="10" height="10" viewBox="0 0 24 24" fill="#fff" aria-hidden="true"><path d="M5 3h4l2 5-2.5 1.5a11 11 0 0 0 6 6L16 13l5 2v4a2 2 0 0 1-2 2A17 17 0 0 1 3 5a2 2 0 0 1 2-2z"/></svg>0400 318 752</li>
      <li><svg width="10" height="10" viewBox="0 0 24 24" fill="none" stroke="#fff" stroke-width="2" aria-hidden="true"><circle cx="12" cy="12" r="10"/><path d="M2 12h20M12 2v20"/></svg>www.tovaniskincare.com</li>
    </ul>
  </div>
</section>

</body>
</html>
```